Full Page Appliance Ad

Create a full page ad (7.5" W x 10" H) representing that we are a full service appliance company, where we have a showroom located at 14 N. Birch Lane Souderton, PA 18970. Our website is www.qrtolvek.com , and our phone number is 215-555-0148. We don't only sell appliances, we deliver, install, and service. We also offer an additional year warranty* (see store for details). In addition to appliances, we also have an Electrical Department that specializes in residential applications.
May be best if split the full page ad into two spots. One spot to reference appliances, and the other to represent electrical.
I want it to look clean, and not too busy
Target Market(s)
30-70 years old
Look and feel

```html
<!DOCTYPE html>
<html lang="en">
<head>
<meta charset="utf-8">
<title>Qrtolvek and Son Inc — Appliances Services</title>
<link rel="stylesheet" href="https://fonts.googleapis.com/css2?family=Bebas+Neue&family=Montserrat:wght@400;500;600;700&family=Heebo:wght@400&display=swap">
<style>
  :root {
    --navy: #1f2452;
    --navy-deep: #1c2a5c;
    --blue: #2a6fba;
    --blue-bright: #2f7fd2;
    --paper: #ffffff;
    --paper-soft: #f3f4f7;
    --ink: #15161c;
    --silver-light: #e6e8ec;
    --silver-mid: #b9bdc4;
    --silver-dark: #7d828b;
  }
  * { box-sizing: border-box; margin: 0; padding: 0; }
  html, body { width: 900px; height: 1200px; overflow: hidden; }
  body { background: var(--paper); font-family: "Montserrat", sans-serif; }

  .ad {
    position: relative;
    width: 900px;
    height: 1200px;
    overflow: hidden;
    background: linear-gradient(180deg, var(--paper-soft) 0%, var(--paper) 40%);
  }

  .wave-band { position: absolute; left: 0; top: 0; width: 900px; height: 1200px; }

  /* Brand */
  .brand {
    position: absolute; left: 0; top: 34px; width: 900px;
    display: flex; align-items: center; justify-content: center; gap: 12px;
  }
  .brand-dot { width: 44px; height: 44px; border-radius: 50%; background: var(--navy); }
  .brand-name { color: var(--navy); font-weight: 700; font-size: 24px; letter-spacing: 0.5px; line-height: 1; }

  /* Headline */
  .headline { position: absolute; left: 0; width: 900px; text-align: center; }
  .headline-main {
    top: 134px; font-family: "Bebas Neue", sans-serif; font-size: 124px; line-height: 1;
    color: var(--blue); letter-spacing: 0; transform: scaleX(0.91);
  }
  .headline-sub {
    top: 234px; font-weight: 600; font-size: 79px; line-height: 1;
    color: var(--navy); letter-spacing: 4px; padding-left: 4px;
  }

  /* Services */
  .service { position: absolute; display: flex; align-items: center; gap: 13px; }
  .service-icon {
    width: 58px; height: 58px; border-radius: 50%;
    background: radial-gradient(circle at 35% 30%, #3566b0 0%, var(--navy-deep) 75%);
    display: flex; align-items: center; justify-content: center;
  }
  .service-icon svg { width: 34px; height: 34px; fill: none; stroke: #fff; stroke-width: 1.6; stroke-linecap: round; stroke-linejoin: round; }
  .service-label { font-weight: 700; font-size: 27px; color: var(--ink); letter-spacing: 0.5px; }
  .service--seller { left: 155px; top: 332px; }
  .service--deliver { left: 155px; top: 396px; }
  .service--install { left: 427px; top: 332px; }
  .service--maint { left: 427px; top: 396px; }

  .product-lineup {
    position: absolute; left: 162px; top: 470px; width: 556px; height: 448px;
    background: linear-gradient(135deg, var(--silver-light) 0%, var(--silver-mid) 55%, var(--silver-dark) 100%);
    border-radius: 6px;
  }

  /* Electrical */
  .electrical-title {
    position: absolute; left: 147px; top: 952px; font-family: "Bebas Neue", sans-serif; font-weight: 400;
    font-size: 50px; line-height: 0.86; color: var(--paper); letter-spacing: -0.5px;
  }
  .electrical-divider { position: absolute; left: 369px; top: 958px; width: 2px; height: 80px; background: var(--paper); }
  .electrical-list {
    position: absolute; top: 965px; list-style: none; color: var(--paper);
    font-family: "Heebo", sans-serif; font-size: 17px; line-height: 22px;
  }
  .electrical-list li { display: flex; align-items: center; gap: 6px; }
  .electrical-list svg { width: 12px; height: 12px; fill: none; stroke: #fff; stroke-width: 1.6; }
  .electrical-list--left { left: 380px; }
  .electrical-list--right { left: 554px; }

  /* Contact */
  .contact-rule { position: absolute; left: 136px; top: 1081px; width: 628px; height: 4px; background: var(--blue-bright); border-radius: 2px; }
  .contact-edge { position: absolute; left: 136px; top: 1081px; width: 3px; height: 86px; background: var(--blue-bright); opacity: 0.6; }
  .contact-call { position: absolute; left: 150px; top: 1092px; color: var(--paper); font-weight: 700; line-height: 1; }
  .contact-call-label { font-size: 27px; letter-spacing: 0.3px; }
  .contact-call-number { font-size: 47px; margin-top: 2px; letter-spacing: -0.5px; }
  .contact-address {
    position: absolute; right: 134px; top: 1093px; text-align: right; color: var(--paper);
    font-size: 24px; line-height: 24px; font-weight: 500; font-style: normal;
  }
  .contact-web { font-weight: 600; margin-top: 2px; display: block; }
</style>
</head>
<body>
<main class="ad">
  <svg class="wave-band" viewBox="0 0 900 1200" aria-hidden="true">
    <defs>
      <linearGradient id="bandFill" x1="0" y1="1" x2="1" y2="0">
        <stop offset="0" stop-color="#2c74c4"/>
        <stop offset="0.55" stop-color="#25498c"/>
        <stop offset="1" stop-color="#1c2a5c"/>
      </linearGradient>
    </defs>
    <path d="M0 650 C 70 610, 160 570, 240 592 C 330 620, 420 690, 560 740 C 700 790, 800 805, 900 834 L 900 1200 L 0 1200 Z" fill="url(#bandFill)"/>
  </svg>

  <header class="brand">
    <span class="brand-dot"></span>
    <span class="brand-name">QRTOLVEK AND SON INC</span>
  </header>

  <h1 class="headline headline-main">APPLIANCES</h1>
  <h2 class="headline headline-sub">SERVICES</h2>

  <div class="service service--seller">
    <span class="service-icon"><svg viewBox="0 0 32 32"><circle cx="16" cy="10" r="5"/><path d="M6 28 v-4 a6 6 0 0 1 6-6 h8 a6 6 0 0 1 6 6 v4 Z"/><path d="M16 18 l-2 4 2 6 2-6 Z"/></svg></span>
    <span class="service-label">SELLER</span>
  </div>
  <div class="service service--deliver">
    <span class="service-icon"><svg viewBox="0 0 32 32"><path d="M8 9 h13 v13 H8"/><path d="M21 13 h5 l3 4 v5 h-8"/><circle cx="12" cy="23" r="2.5"/><circle cx="24" cy="23" r="2.5"/><path d="M2 13 h6 M4 17 h4 M2 21 h4"/></svg></span>
    <span class="service-label">DELIVER</span>
  </div>
  <div class="service service--install">
    <span class="service-icon"><svg viewBox="0 0 32 32"><path d="M6 26 L18 14"/><path d="M18 14 a5 5 0 1 1 5 -8 l-3 3 2 2 3-3 a5 5 0 0 1 -7 6"/><path d="M9 6 l4 4 M11 12 l10 14"/></svg></span>
    <span class="service-label">INSTALLTION</span>
  </div>
  <div class="service service--maint">
    <span class="service-icon"><svg viewBox="0 0 32 32"><circle cx="16" cy="16" r="9"/><path d="M16 3 v4 M16 25 v4 M3 16 h4 M25 16 h4 M7 7 l3 3 M22 22 l3 3 M25 7 l-3 3 M10 22 l-3 3"/><path d="M12 16 l3 3 5-6"/></svg></span>
    <span class="service-label">MAINTENANCE</span>
  </div>

  <div class="product-lineup" role="img" aria-label="Group of stainless steel appliances: refrigerators, dishwasher, oven, washing machine, microwave, coffee machine, blender and toaster"></div>

  <h3 class="electrical-title">NEED AN<br>ELECTRICIAN?</h3>
  <span class="electrical-divider"></span>
  <ul class="electrical-list electrical-list--left">
    <li><svg viewBox="0 0 12 12"><circle cx="6" cy="6" r="5"/><path d="M3.5 6 l2 2 3-4"/></svg>Troubleshooting</li>
    <li><svg viewBox="0 0 12 12"><circle cx="6" cy="6" r="5"/><path d="M3.5 6 l2 2 3-4"/></svg>Service Upgrades</li>
    <li><svg viewBox="0 0 12 12"><circle cx="6" cy="6" r="5"/><path d="M3.5 6 l2 2 3-4"/></svg>Kitchen Remodels</li>
  </ul>
  <ul class="electrical-list electrical-list--right">
    <li><svg viewBox="0 0 12 12"><circle cx="6" cy="6" r="5"/><path d="M3.5 6 l2 2 3-4"/></svg>Under Cabinet Lighting</li>
    <li><svg viewBox="0 0 12 12"><circle cx="6" cy="6" r="5"/><path d="M3.5 6 l2 2 3-4"/></svg>Surge Protection</li>
    <li><svg viewBox="0 0 12 12"><circle cx="6" cy="6" r="5"/><path d="M3.5 6 l2 2 3-4"/></svg>Celling Fan Installation</li>
  </ul>

  <span class="contact-rule"></span>
  <span class="contact-edge"></span>
  <div class="contact-call">
    <div class="contact-call-label">GIVE US A CALL</div>
    <div class="contact-call-number">215-555-0148</div>
  </div>
  <address class="contact-address">
    14 N. Birch Lane<br>Fernhollow, PA 18970
    <span class="contact-web">www.qrtolvek.com</span>
  </address>
</main>
</body>
</html>
```